advertisement for The Willow Path

want a postcard size ad for our web and print for our corporate Church Willow Path event

fancy text on graphic or referring t the biblical art of fasting

Target Market(s)

members of the church and people that maybe interesting in clicking on the link on our facebook or web page.

Industry/Entity Type

Advertising

Requirements
Must have
• beautiful text " the Willow Path, a 21 Day Experience with God" Join us!!
and graphics that make the mini flier pop
Nice to have
• background relating to fasting or scriptures

```html
<!DOCTYPE html>
<html lang="en">
<head>
<meta charset="utf-8">
<title>The Willow Path – A 21 Day Experience with God</title>
<link href="https://fonts.googleapis.com/css2?family=Rubik+Dirt&family=Cabin:wght@700&display=swap" rel="stylesheet">
<style>
  :root {
    --sky-light: #fbf6c8;
    --sky-gold: #f0c64a;
    --ember: #c8561c;
    --deep-red: #8a1410;
    --wine: #4e0508;
    --ink: #111010;
    --white: #ffffff;
    --gold-accent: #d2ad3e;
  }
  * { margin: 0; padding: 0; box-sizing: border-box; }
  html, body { width: 1200px; height: 848px; overflow: hidden; background: var(--wine); }
  .postcard {
    position: relative;
    width: 1200px;
    height: 848px;
    overflow: hidden;
  }
  .scene {
    position: absolute;
    inset: 0;
    background:
      radial-gradient(ellipse 420px 360px at 140px 300px, rgba(255,255,240,0.95), rgba(255,255,240,0) 70%),
      radial-gradient(ellipse 380px 300px at 200px 680px, rgba(214,160,70,0.75), rgba(214,160,70,0) 70%),
      linear-gradient(160deg, var(--sky-light) 0%, var(--sky-gold) 32%, #e49a2c 50%, var(--ember) 62%, var(--deep-red) 78%, var(--wine) 100%);
  }
  .title {
    position: absolute;
    left: 66px;
    top: 40px;
    width: 680px;
    height: 470px;
  }
  .title text {
    font-family: "Rubik Dirt", "Impact", sans-serif;
    fill: var(--ink);
  }
  .host {
    position: absolute;
    top: 58px;
    right: 86px;
    display: flex;
    align-items: center;
    gap: 10px;
    font-family: "Cabin", sans-serif;
    font-weight: 700;
    font-size: 40px;
    letter-spacing: -0.5px;
    color: var(--ink);
  }
  .host-dot {
    width: 14px;
    height: 14px;
    border-radius: 50%;
    background: var(--ink);
  }
  .invite {
    position: absolute;
    right: 86px;
    top: 652px;
    text-align: right;
    font-family: "Cabin", sans-serif;
    font-weight: 700;
    font-size: 47px;
    line-height: 56px;
    color: var(--white);
  }
  .invite-cta { color: var(--gold-accent); }
</style>
</head>
<body>
  <main class="postcard">
    <div class="scene" role="img" aria-label="Sunset photograph: golden sky with a faint cross of light, windswept grass turning deep red, and clasped praying hands in the lower left"></div>

    <svg class="title" viewBox="0 0 680 470" aria-label="The Willow Path">
      <text x="4" y="118" font-size="150" textLength="330" lengthAdjust="spacingAndGlyphs">THE</text>
      <text x="0" y="288" font-size="196" textLength="655" lengthAdjust="spacingAndGlyphs">WILLOW</text>
      <text x="0" y="452" font-size="196" textLength="470" lengthAdjust="spacingAndGlyphs">PATH</text>
    </svg>

    <div class="host">
      <span class="host-dot" aria-hidden="true"></span>
      <span class="host-name">Brightwater Church</span>
    </div>

    <p class="invite">
      A 21 Day Experience<br>
      with God. <span class="invite-cta">JOIN US!</span>
    </p>
  </main>
</body>
</html>
```